Website R86 coffee

I am opening a small business selling locally roasted coffee online. To start with I want a site with three pages. 1. A welcome page with logo and mission/vision. 2. Shopping/ordering page. 3. About Us page. The brand is "R86 Coffee - A warm start to every day". We are giving back to the downs syndrome community by employing people with down syndrome (Trisomy 21) and buy donating to down syndrome research.

Target Market(s)

Families and friends of people with downs syndrome

Coding

Coded - Design and coding required

Number of Pages Required

3 page

```html
<!DOCTYPE html>
<html lang="en">
<head>
<meta charset="utf-8">
<title>R86 Coffee</title>
<link href="https://fonts.googleapis.com/css2?family=Nunito:wght@400;600&family=Roboto+Condensed:wght@400&display=swap" rel="stylesheet">
<style>
  :root {
    --paper: #f3ebe1;
    --ink: #2b2b2b;
    --body: #3d3d3d;
    --accent: #a87c5a;
    --card: #f4f4f4;
    --rule: #d9d2c9;
    --dark: #2c2926;
    --muted: #8a8a8a;
  }
  * { box-sizing: border-box; margin: 0; padding: 0; }
  html, body { width: 1200px; height: 3045px; overflow: hidden; }
  body { position: relative; background: #fff; font-family: "Nunito", sans-serif; color: var(--body); }
  .abs { position: absolute; }

  .site-header { left: 0; top: 0; width: 1200px; height: 126px; background: var(--paper); }
  .brand { left: 189px; top: 24px; display: flex; flex-direction: column; gap: 4px; }
  .brand-name { display: flex; align-items: center; gap: 12px; font-size: 34px; font-weight: 400; color: var(--ink); line-height: 1.2; }
  .brand-mark { width: 18px; height: 18px; background: var(--ink); }
  .brand-tagline { font-size: 11px; letter-spacing: 1.5px; text-transform: uppercase; color: var(--ink); padding-left: 30px; }
  .contact-bar { right: 188px; top: 24px; display: flex; gap: 18px; font-size: 13px; color: var(--ink); align-items: center; }
  .contact-bar span { display: flex; align-items: center; gap: 8px; }
  .main-nav { left: 611px; top: 70px; display: flex; align-items: center; gap: 38px; font-size: 13px; color: var(--ink); }
  .main-nav .current { font-weight: 600; border-bottom: 2px solid var(--ink); padding-bottom: 3px; }
  .cart { display: flex; align-items: center; gap: 8px; }
  .cart-icon { width: 26px; height: 26px; background: var(--accent); display: flex; align-items: center; justify-content: center; }

  .hero { left: 0; top: 126px; width: 1200px; height: 459px;
    background: radial-gradient(circle at 78% 45%, #6b3a22 0 16%, transparent 30%),
                linear-gradient(100deg, #2f4a1c 0%, #4f6b25 30%, #6e4a28 60%, #3b2a1e 100%); }
  .hero-title { left: 189px; top: 272px; width: 420px; font-family: "Roboto Condensed", sans-serif; font-size: 40px; font-weight: 400; line-height: 55px; color: #fff; }
  .hero-btn { left: 189px; top: 382px; border: 2px solid #1e1e1e; padding: 4px 10px; font-size: 16px; color: #fff; background: rgba(0,0,0,.2); }

  .welcome-photo { left: 195px; top: 677px; width: 240px; height: 240px; border-radius: 50%;
    background: radial-gradient(circle at 50% 50%, #c9a57e 0 18%, #f3f1ee 19% 60%, #e6e3df 100%); box-shadow: 0 8px 24px rgba(0,0,0,.08); }
  .welcome-text { left: 539px; top: 667px; width: 475px; }
  .welcome-text h1 { font-size: 36px; font-weight: 400; color: var(--ink); margin-bottom: 14px; }
  .welcome-text p { font-size: 14px; line-height: 25.5px; margin-bottom: 9px; }
  .link { color: var(--accent); border-bottom: 1px solid var(--accent); padding-bottom: 2px; }
  .welcome-text .link { display: inline-block; margin-top: 16px; font-size: 16px; }

  .products-head { left: 0; top: 1110px; width: 1200px; text-align: center; }
  .products-head h2 { font-size: 35px; font-weight: 400; color: var(--ink); margin-bottom: 12px; }
  .products-head p { width: 690px; margin: 0 auto; font-size: 14px; line-height: 25px; }

  .card { width: 403px; height: 494px; background: var(--card); }
  .card-photo { position: absolute; left: 120px; top: 56px; width: 172px; height: 300px; border-radius: 10px 10px 14px 14px; }
  .card h3 { position: absolute; top: 376px; width: 100%; text-align: center; font-size: 16px; font-weight: 400; color: var(--ink); }
  .card p { position: absolute; top: 408px; left: 20px; right: 20px; text-align: center; font-size: 13px; line-height: 21px; }
  .card .price { position: absolute; left: 20px; top: 462px; font-size: 16px; color: var(--accent); }
  .card .link { position: absolute; right: 20px; top: 458px; font-size: 14px; }
  .bag-cup { background: linear-gradient(180deg, #b98a66 0%, #a5754f 70%, #9a6c48 100%); }
  .bag-leaf { background: linear-gradient(180deg, #b98a66 0%, #a5754f 60%, #2c2c2c 61%, #1e1e1e 100%); }
  .bag-white { background: linear-gradient(180deg, #f2f1ef 0%, #e8e4de 60%, #cdb597 61%, #bfa585 100%); }

  .giving { left: 0; top: 2352px; width: 1200px; height: 444px; background: radial-gradient(ellipse at 50% 50%, #3a3430 0%, var(--dark) 70%, #1f1c1a 100%); }
  .giving-text { left: 225px; top: 2488px; width: 750px; text-align: center; font-size: 23px; line-height: 41px; color: #fff; }
  .giving-link { left: 0; top: 2630px; width: 1200px; text-align: center; font-size: 16px; }

  .footer-brand { left: 189px; top: 2880px; border: 2px solid var(--ink); padding: 10px 20px; }
  .footer-brand .brand-name { font-size: 36px; }
  .footer-cup { left: 556px; top: 2880px; width: 78px; height: 78px; }
  .footer-nav { right: 189px; top: 2882px; display: flex; gap: 36px; font-size: 13px; color: var(--ink); }
  .footer-nav .current { font-weight: 600; }
  .follow { right: 186px; top: 2920px; display: flex; align-items: center; gap: 4px; font-size: 13px; color: var(--ink); }
  .follow .label { margin-right: 18px; }
  .social { width: 31px; height: 31px; border: 1px solid #9a9a9a; display: flex; align-items: center; justify-content: center; }
  .social-dot { width: 12px; height: 12px; border-radius: 50%; background: var(--muted); }
  .footer-rule { left: 189px; top: 2997px; width: 824px; height: 1px; background: var(--rule); }
  .copyright { left: 0; top: 3013px; width: 1200px; text-align: center; font-size: 13px; color: var(--ink); }
</style>
</head>
<body>
  <header class="site-header abs">
    <div class="brand abs">
      <span class="brand-name"><span class="brand-mark"></span>R86 Coffee</span>
      <span class="brand-tagline">A warm start to every day</span>
    </div>
    <div class="contact-bar abs">
      <span><svg width="20" height="20" viewBox="0 0 24 24" fill="none" stroke="#2b2b2b" stroke-width="1.5"><path d="M5 3h4l2 5-3 2a12 12 0 0 0 6 6l2-3 5 2v4a2 2 0 0 1-2 2A18 18 0 0 1 3 5a2 2 0 0 1 2-2z"/></svg>Call Us: +1 (555) 204-8619</span>
      <span><svg width="22" height="18" viewBox="0 0 24 18" fill="none" stroke="#2b2b2b" stroke-width="1.5"><rect x="1" y="1" width="22" height="16"/><path d="M1 1l11 9 11-9"/></svg>hello@r86coffee.example</span>
    </div>
    <nav class="main-nav abs">
      <span class="current">Home</span>
      <span>Shop Our Products</span>
      <span>About Us</span>
      <span class="cart"><span class="cart-icon"><svg width="16" height="14" viewBox="0 0 16 14" fill="none" stroke="#fff" stroke-width="1.4"><path d="M1 1h2l2 8h8l2-6H4"/><circle cx="6" cy="12" r="1"/><circle cx="12" cy="12" r="1"/></svg></span>Cart (0)</span>
    </nav>
  </header>

  <section class="hero abs" role="img" aria-label="Photo of a cup of latte beside ripe coffee cherries on the branch"></section>
  <h2 class="hero-title abs">We are a Boutique Coffee Roaster in Australia</h2>
  <span class="hero-btn abs">Shop Now</span>

  <div class="welcome-photo abs" role="img" aria-label="Top-down photo of a latte with heart latte art in a white cup"></div>
  <section class="welcome-text abs">
    <h1>Welcome to R86 Coffee</h1>
    <p>Lorem ipsum dolor sit amet, consectetuer adipiscing elit, sed diam nonummy nibh euismod tincidunt ut laoreet dolore magna aliquam erat volutpat. Ut wisi enim ad minim veniam, quis nostrud exerci tation ullamcorper suscipit lobortis nisl ut aliquip ex ea commodo consequat.</p>
    <p>Duis autem vel eum iriure dolor in hendrerit in vulputate velit esse molestie consequat, vel illum dolore eu feugiat nulla facilisis at vero eros et accumsan et iusto odio dignissim qui blandit praesent luptatum zzril delenit augue duis dolore te feugait nulla facilisi.</p>
    <span class="link">Read More About Our Mission &amp; Vision</span>
  </section>

  <section class="products-head abs">
    <h2>Our Products</h2>
    <p>Lorem ipsum dolor sit amet, consectetuer adipiscing elit, sed diam nonummy nibh euismod tincidunt ut laoreet dolore magna aliquam erat volutpat ut wisi enim ad minim .</p>
  </section>

  <article class="card abs" style="left:189px;top:1241px">
    <div class="card-photo bag-cup" role="img" aria-label="Kraft coffee pouch with a sketched cup illustration"></div>
    <h3>Product Name 1</h3>
    <p>Lorem ipsum dolor sit amet, consectetuer adipiscing lorem ipsum dolor sit amet, consectetuer adipiscing</p>
    <span class="price">$ 12.45</span><span class="link">View Details</span>
  </article>
  <article class="card abs" style="left:610px;top:1241px">
    <div class="card-photo bag-leaf" role="img" aria-label="Kraft and black coffee pouch with a coffee plant illustration"></div>
    <h3>Product Name 2</h3>
    <p>Lorem ipsum dolor sit amet, consectetuer adipiscing lorem ipsum dolor sit amet, consectetuer adipiscing</p>
    <span class="price">$ 12.45</span><span class="link">View Details</span>
  </article>
  <article class="card abs" style="left:189px;top:1771px">
    <div class="card-photo bag-leaf" role="img" aria-label="Kraft and black coffee pouch with a coffee plant illustration"></div>
    <h3>Product Name 3</h3>
    <p>Lorem ipsum dolor sit amet, consectetuer adipiscing lorem ipsum dolor sit amet, consectetuer adipiscing</p>
    <span class="price">$ 12.45</span><span class="link">View Details</span>
  </article>
  <article class="card abs" style="left:610px;top:1771px">
    <div class="card-photo bag-white" role="img" aria-label="White and beige coffee pouch with a sketched cup illustration"></div>
    <h3>Product Name 4</h3>
    <p>Lorem ipsum dolor sit amet, consectetuer adipiscing lorem ipsum dolor sit amet, consectetuer adipiscing</p>
    <span class="price">$ 12.45</span><span class="link">View Details</span>
  </article>

  <section class="giving abs" role="img" aria-label="Dark photo of roasted coffee beans and rope"></section>
  <p class="giving-text abs">We are giving back to the downs syndrome community by employing people with down syndrome (Trisomy 21) and buy donating to down syndrome research.</p>
  <div class="giving-link abs"><span class="link">Shop Now</span></div>

  <footer>
    <div class="footer-brand abs">
      <span class="brand-name"><span class="brand-mark"></span>R86 Coffee</span>
      <span class="brand-tagline">A warm start to every day</span>
    </div>
    <div class="footer-cup abs" role="img" aria-label="Faint steaming coffee cup decoration" style="background:radial-gradient(circle at 50% 65%, #ececec 0 45%, transparent 46%)"></div>
    <nav class="footer-nav abs"><span class="current">Home</span><span>Shop Our Products</span><span>About Us</span></nav>
    <div class="follow abs"><span class="label">Follow Us On</span>
      <span class="social" aria-label="Social link 1"><span class="social-dot"></span></span>
      <span class="social" aria-label="Social link 2"><span class="social-dot"></span></span>
      <span class="social" aria-label="Social link 3"><span class="social-dot"></span></span>
      <span class="social" aria-label="Social link 4"><span class="social-dot"></span></span>
    </div>
    <div class="footer-rule abs"></div>
    <p class="copyright abs">© 2021 R86 Coffee. All Rights Reserved.</p>
  </footer>
</body>
</html>
```